Corvell Executive Search - New Business Card Design Project

We are an executive search firm called Corvell Executive Search based in the UK. We require a custom design for a business card. We're looking to convey a professional service to executives for executive search recruitment services. In terms of colours, we like dark blues and grays (maybe even silver incorporated somewhere if we go for a foiled type of card) but we're open to your artistic flare. See our current logo in attachments. We are totally open on design so long as the design is slick and professional.
Updates

Thanks for all your contributions of various designs. I have to say the quality of work has been amazing which is going to make our job quite difficult in the coming days on making a decision. Thanks to you all that have taken the time to submit designs thus far. We'll keep on reviewing and try to narrow down our selection as soon as possible.

Target Market(s)

Executive Search

Industry/Entity Type

Recruitment

Contact Information for Business Card

Corvell Executive Search,
Exclusively Sourcing & Hiring Senior Leaders
Dominic Haverley, Managing Director,
07742 318906
0117 468 2917
dominic@corvellexecutive.example
corvellexecutive.example
47 Linden Court, Marsh Lane, Bristol, BS9 7QT

Font styles to use
Sans Serif
Other font styles liked:
• Roboto (which is used in our logo)

Requirements
Must have
• Our logo (It has a subtle fade on it from #02071d at top to #333649 at bottom)
• The logo can be on one side or both sides
• Must be elegant and professional
• We have 2nd slogan CONSULT | INSPIRE | INNOVATE | DELIVER which can be incorporated into the card
Nice to have
• Use of blues and grey colours
• Compatible with similar styling to our website corvellexecutive.example
Should not have
• Must not be overly brash
• Must not contain cartoon characters

```html
<!DOCTYPE html>
<html lang="en">
<head>
<meta charset="utf-8">
<title>Corvell Executive Search – Business Card</title>
<link rel="stylesheet" href="https://fonts.googleapis.com/css2?family=Roboto:wght@400;500;700&display=swap">
<style>
  :root {
    --bg: #d9d9db;
    --navy-top: #02071d;
    --navy-mid: #1a1e35;
    --navy-bottom: #333649;
    --white: #ffffff;
    --accent: #2e9df0;
    --text-grey: #5c5f66;
    --rule-grey: #8c8e94;
  }
  * { margin: 0; padding: 0; box-sizing: border-box; }
  html, body {
    width: 1200px; height: 1000px; overflow: hidden;
    background: var(--bg);
    font-family: "Roboto", Arial, sans-serif;
  }
  .canvas { position: relative; width: 1200px; height: 1000px; }

  .card {
    position: absolute; left: 263px; width: 674px;
    box-shadow: 0 6px 16px rgba(0,0,0,0.25);
    overflow: hidden;
  }

  /* Front */
  .card--front {
    top: 58px; height: 418px;
    background: linear-gradient(150deg, var(--navy-top) 0%, var(--navy-mid) 45%, var(--navy-bottom) 100%);
  }
  .card--front .sheen {
    position: absolute; inset: 0;
    background: linear-gradient(120deg, transparent 52%, rgba(255,255,255,0.06) 62%, transparent 75%);
  }
  .front-brand {
    position: absolute; left: 26px; top: 290px;
    color: var(--white); font-weight: 500;
    font-size: 40px; line-height: 1.1; letter-spacing: 0.5px;
  }
  .front-tagline {
    position: absolute; left: 26px; top: 380px;
    font-size: 13px; color: var(--accent); letter-spacing: 0.3px;
  }

  /* Back */
  .card--back { top: 532px; height: 421px; background: var(--white); }
  .brand-mark {
    position: absolute; left: 25px; top: 26px;
    display: flex; align-items: flex-end; gap: 16px;
  }
  .brand-mark__square {
    width: 108px; height: 108px; flex: none;
    background: linear-gradient(180deg, var(--navy-top), var(--navy-bottom));
  }
  .brand-mark__name {
    font-size: 18px; font-weight: 500; color: var(--navy-mid);
    line-height: 1; padding-bottom: 4px;
  }

  .person {
    position: absolute; right: 365px; top: 215px; text-align: right;
  }
  .person__name { font-size: 20px; font-weight: 500; color: var(--accent); line-height: 1.1; }
  .person__role { font-size: 16.5px; color: var(--text-grey); margin-top: 5px; }

  .divider {
    position: absolute; left: 337px; top: 222px; width: 1.5px; height: 144px; background: var(--rule-grey);
  }

  .contact { position: absolute; left: 366px; top: 215px; color: var(--text-grey); font-size: 17px; }
  .contact__address { line-height: 24px; }
  .contact__list { list-style: none; margin-top: 11px; }
  .contact__list li { display: flex; align-items: center; height: 24.5px; }
  .contact__list svg { width: 12px; height: 12px; margin: 0 8px 0 1px; fill: var(--accent); flex: none; }

  .footer-rule {
    position: absolute; left: 0; right: 0; top: 402px; height: 2px; background: var(--accent);
  }
  .footer-band {
    position: absolute; left: 0; right: 0; top: 406px; height: 15px;
    background: linear-gradient(90deg, var(--navy-top), var(--navy-bottom));
  }
</style>
</head>
<body>
<main class="canvas">

  <section class="card card--front" aria-label="Card front">
    <div class="sheen"></div>
    <h1 class="front-brand">Corvell Executive Search</h1>
    <p class="front-tagline">Exclusively Sourcing &amp; Hiring Senior Leaders</p>
  </section>

  <section class="card card--back" aria-label="Card back">
    <div class="brand-mark">
      <div class="brand-mark__square" aria-hidden="true"></div>
      <span class="brand-mark__name">Corvell Executive Search</span>
    </div>

    <div class="person">
      <p class="person__name">Dominic Haverley</p>
      <p class="person__role">Managing Director</p>
    </div>

    <div class="divider"></div>

    <div class="contact">
      <p class="contact__address">47 Linden Court, Marsh Lane,<br>Bristol, BS9 7QT</p>
      <ul class="contact__list">
        <li>
          <svg viewBox="0 0 12 12" aria-hidden="true"><path d="M2.2 0.8l2 2-1 1.3c0.7 1.6 1.9 2.8 3.5 3.5l1.3-1 2 2-1.4 1.9C4.6 10.2 1.8 7.4 0.5 2.2z"/></svg>
          07742 318906
        </li>
        <li>
          <svg viewBox="0 0 12 12" aria-hidden="true"><path d="M3 0.5h6v3H3z M1 4h10v5H9V7H3v2H1z M3.5 7.5h5V11.5h-5z"/></svg>
          0117 468 2917
        </li>
        <li>
          <svg viewBox="0 0 12 12" aria-hidden="true"><path d="M0.5 2.5h11v7h-11z"/><path d="M0.8 2.8L6 6.8l5.2-4" fill="none" stroke="#fff" stroke-width="1"/></svg>
          dominic@corvellexecutive.example
        </li>
        <li>
          <svg viewBox="0 0 12 12" aria-hidden="true"><circle cx="6" cy="6" r="5.5"/><path d="M0.5 6h11M6 0.5v11M2 3h8M2 9h8" stroke="#fff" stroke-width="0.7" fill="none"/><ellipse cx="6" cy="6" rx="2.3" ry="5.5" fill="none" stroke="#fff" stroke-width="0.7"/></svg>
          corvellexecutive.example
        </li>
      </ul>
    </div>

    <div class="footer-rule"></div>
    <div class="footer-band"></div>
  </section>

</main>
</body>
</html>
```